Tour agency for FIT and groups need a business card design

We need a business card design for a tour agency company that is based in Perth called" BRISK NO", we aim to provide customise, unique and seamless travel arrangement for FIT and groups. We serve both high profile businessperson, government authorities, business partners, executives and investors. The name card should be more professional looking.
Updates

Project Deadline Extended Reason: Have some changes that needed to make, director will be back to office on Monday, sorry for the inconvenience cause. Added Saturday, May 6, 2017

Target Market(s)

High profile businessperson, government authorities, business partners, executives and investors.

Industry/Entity Type

Tourism

Contact Information for Business Card

Brisk NO
Level 1, 214 Marlowe Avenue, Dunreath NO, 6120
www.briskno.com.au

Font styles to use
Serif

Colors

Designer to choose colors to be used in the design.

Requirements
Must have
• My project must have a company logo
Nice to have
• a more professional and solid yet friendly name card design. We may want to include chinese name in the name card as well. Edge of the card can be filled with gold and we think that transparent name cards are interesting.

```html
<!DOCTYPE html>
<html lang="en">
<head>
<meta charset="utf-8">
<title>Brisk NO – Business Card</title>
<link rel="stylesheet" href="https://fonts.googleapis.com/css2?family=Cormorant+Garamond:wght@400;500;600&family=Noto+Serif+TC:wght@500;700&display=swap">
<style>
  :root {
    --backdrop: #ece7df;
    --card-paper: #f1ece4;
    --card-edge: #d9d1c4;
    --ink: #2f2f2c;
    --ink-soft: #5a5852;
    --brand-teal: #2a8fb0;
    --band-dark: #23241f;
    --band-text: #efe6cf;
    --frame-line: #4a4a46;
  }
  * { box-sizing: border-box; margin: 0; padding: 0; }
  html, body { width: 1200px; height: 1000px; overflow: hidden; }
  body {
    background: var(--backdrop);
    font-family: "Cormorant Garamond", Georgia, serif;
    color: var(--ink);
  }
  .canvas {
    width: 1200px; height: 1000px;
    display: flex; align-items: center; justify-content: center; gap: 90px;
  }
  .card {
    position: relative;
    width: 340px; height: 560px;
    background: linear-gradient(160deg, #f6f2ec 0%, var(--card-paper) 55%, #e8e1d6 100%);
    border: 1px solid var(--card-edge);
    box-shadow: 0 18px 40px rgba(60, 45, 30, 0.12);
  }

  /* Front */
  .front-frame {
    position: absolute; left: 66px; top: 138px;
    width: 208px; height: 168px;
    border: 1.5px solid var(--frame-line);
    display: flex; align-items: center; justify-content: center;
  }
  .brand-name {
    font-family: "Cormorant Garamond", Georgia, serif;
    font-weight: 600;
    color: var(--brand-teal);
    letter-spacing: 1px;
  }
  .front-frame .brand-name { font-size: 40px; }
  .chinese-name {
    font-family: "Noto Serif TC", "Songti TC", serif;
    font-weight: 700;
    letter-spacing: 6px;
  }
  .front-chinese {
    position: absolute; top: 330px; left: 0; right: 0;
    text-align: center; font-size: 42px; color: var(--ink);
  }

  /* Back */
  .back-band {
    position: absolute; left: 0; top: 50px;
    width: 185px; height: 64px;
    background: var(--band-dark);
    display: flex; align-items: center; justify-content: center;
  }
  .back-band .chinese-name { font-size: 38px; color: var(--band-text); }
  .contact-block {
    position: absolute; top: 208px; left: 0; right: 0;
    text-align: center;
  }
  .person-name { font-size: 24px; font-weight: 500; letter-spacing: 0.5px; }
  .address { font-size: 12.5px; color: var(--ink-soft); margin-top: 2px; }
  .contact-list {
    list-style: none; margin: 26px 0 0 80px; text-align: left;
  }
  .contact-item {
    display: flex; align-items: center; gap: 30px;
    font-size: 14px; color: var(--ink-soft); height: 40px;
  }
  .contact-item svg { width: 22px; height: 22px; flex: none; }
  .website {
    margin-top: 22px; font-size: 14px; color: var(--ink-soft); letter-spacing: 1px;
  }
  .back-brand {
    position: absolute; right: 14px; bottom: 18px;
    font-size: 30px;
  }
</style>
</head>
<body>
<main class="canvas">

  <section class="card card-front" aria-label="Business card front">
    <div class="front-frame">
      <span class="brand-name">Brisk NO</span>
    </div>
    <p class="chinese-name front-chinese" lang="zh-Hant">迅諾行</p>
  </section>

  <section class="card card-back" aria-label="Business card back">
    <div class="back-band">
      <span class="chinese-name" lang="zh-Hant">迅諾行</span>
    </div>
    <div class="contact-block">
      <p class="person-name">Brisk NO</p>
      <p class="address">Level 1, 214 Marlowe Avenue, Dunreath NO, 6120</p>
      <ul class="contact-list">
        <li class="contact-item">
          <svg viewBox="0 0 24 24" fill="none" stroke="#5a5852" stroke-width="1.4" aria-hidden="true">
            <circle cx="12" cy="12" r="4"/>
            <path d="M16 8v5.5a2.5 2.5 0 0 0 5 0V12a9 9 0 1 0-3.5 7.1"/>
          </svg>
          <span>info@briskno.com.au</span>
        </li>
        <li class="contact-item">
          <svg viewBox="0 0 24 24" fill="none" stroke="#5a5852" stroke-width="1.4" aria-hidden="true">
            <rect x="6" y="2.5" width="12" height="19" rx="1.5"/>
            <line x1="10" y1="18.5" x2="14" y2="18.5"/>
          </svg>
          <span>+61 8 5550 1427</span>
        </li>
      </ul>
      <p class="website">www.briskno.com.au</p>
    </div>
    <span class="brand-name back-brand">Brisk NO</span>
  </section>

</main>
</body>
</html>
```